House Builder and Property Development Card Design and Logo

I need a business card design for a building and property development company.
Colour scheme of Dark Grey and Green, I would like it bold, sharp and professional.
No logo yet done, I'm open to options but please stay away from the usual- house, roof, hammers etc.
Thanks Rob

Please be aware that on the business card information section the WHRC # 5528391 is a licence number and my phone number 0492837165. The numbers are close together and could be mistaken as one whole number 

Thank you

                                   

Industry/Entity Type

Building

Contact Information for Business Card

VARGA BUILD & DEVELOPMENT.
Residential Building & Property Development
Robert Varga - Director
WHRC # 5528391
0492837165
rob@vargabuild.example.com.au

Requirements
Must have
• Bold Business name
Dark grey and green colours
Should not have
• roof outline or hammer logo

```html
<!DOCTYPE html>
<html lang="en">
<head>
<meta charset="utf-8">
<title>Varga Build &amp; Development – Business Card</title>
<link rel="stylesheet" href="https://fonts.googleapis.com/css2?family=PT+Sans:wght@400;700&display=swap">
<style>
  :root {
    --bg: #2b2b2c;
    --green-dark: #0b3a2c;
    --green-mid: #125c44;
    --green-light: #1c7357;
    --white: #ffffff;
    --paper: #f1f1f1;
    --paper-shade: #d9d9d9;
    --text-soft: #c9d8d1;
  }
  * { box-sizing: border-box; margin: 0; padding: 0; }
  html, body {
    width: 1200px; height: 900px; overflow: hidden;
    background: var(--bg);
  }
  .stage { position: relative; width: 1200px; height: 900px; }
  .card {
    position: absolute; left: 335px;
    width: 530px; height: 303px;
    overflow: hidden;
  }

  /* Back of card */
  .card--back {
    top: 110px;
    background: linear-gradient(160deg, var(--green-dark) 0%, var(--green-mid) 60%, var(--green-light) 100%);
    display: flex; align-items: center; justify-content: center;
  }
  .card--back .brand-name {
    font-family: "PT Sans", sans-serif; font-weight: 400;
    color: var(--white); font-size: 26px;
    letter-spacing: 3px; white-space: nowrap;
  }

  /* Front of card */
  .card--front {
    top: 487px;
    background: linear-gradient(180deg, var(--white) 0%, var(--paper) 70%, var(--paper-shade) 100%);
  }
  .card--front .band {
    position: absolute; left: 0; right: 0; top: 92px; height: 128px;
    background: var(--green-dark);
  }
  .card--front .contact {
    position: absolute; left: 32px; top: 108px;
    font-family: "PT Sans", sans-serif; color: var(--white);
  }
  .card--front .contact__name {
    font-weight: 700; font-size: 17px; margin-bottom: 22px;
  }
  .card--front .contact__line {
    font-size: 12.5px; line-height: 1.45; color: var(--text-soft);
  }
  .card--front .band__divider {
    position: absolute; left: 320px; top: 112px;
    width: 2px; height: 88px; background: rgba(255,255,255,0.8);
  }
  .card--front .brand-name {
    position: absolute; left: 322px; right: 0; top: 145px;
    text-align: center;
    font-family: "PT Sans", sans-serif; font-weight: 700;
    font-size: 18px; color: var(--white); letter-spacing: 3px;
  }
</style>
</head>
<body>
<main class="stage">
  <section class="card card--back" aria-label="Card back">
    <p class="brand-name">VARGA BUILD &amp; DEVELOPMENT</p>
  </section>

  <section class="card card--front" aria-label="Card front">
    <div class="band"></div>
    <div class="contact">
      <p class="contact__name">Robert Varga - Director</p>
      <p class="contact__line">WHRC # 5528391</p>
      <p class="contact__line">Phone: 0492837165</p>
      <p class="contact__line">Email: rob@vargabuild.example.com.au</p>
    </div>
    <div class="band__divider"></div>
    <p class="brand-name">VARGA</p>
  </section>
</main>
</body>
</html>
```